Copper Vale Winery wants innovative label for unique bottling

We are looking for a lable for a champagne which is made of Eiswein (Ice Wine; this is what you get when you harvest the grapes at temperatures below -7 degrees celsius. the water is frozen and you only get the pure extract out of the grapes (sugar, acid and all the aromas). even after fermentation is remains very sweet. we then turned it into champagne (2nd fermentation in bottles for another 12 months and so on and so forth). It is bottled in small champagne bottles (0,375 l). Dark green (just like a champagne bottle). The name of the product is "Glintova" (from Freeze and Riesling). So it is unique, it is sparkling, it is sweet, it is full of aromas and it is produced from deep frozen grapes. All of this hopefully creates ideas in your imagination which lead to great designs! The only word printed onto the label is "Glintova". The colour code should still be recognizable. See www.brandt-wolmer.de for our standard labels and bottles. you can also download label designs and colours. we prefer modern / fresh / light design rather than traditional, flowery, pittoresque. But please not 100 different colours or screaming colours. You may also imagine transparent labels. Up to you! Have fun!

```html
<!DOCTYPE html>
<html lang="en">
<head>
<meta charset="utf-8">
<title>Glintova label – presentation</title>
<link rel="stylesheet" href="https://fonts.googleapis.com/css2?family=Didact+Gothic&display=swap">
<style>
  :root {
    --canvas-white: #ffffff;
    --canvas-green: #66823a;
    --frame-orange: #f39325;
    --label-white: #ffffff;
    --name-grey: #5b5b5d;
    --peak-blue: #11587f;
    --stripe-brown: #8a5a2e;
    --stripe-glow: #fbf7a6;
  }
  html, body {
    margin: 0;
    padding: 0;
    width: 1200px;
    height: 1000px;
    overflow: hidden;
  }
  .canvas {
    position: relative;
    width: 1200px;
    height: 1000px;
    background: var(--canvas-white);
  }
  .backdrop-green {
    position: absolute;
    left: 0;
    top: 500px;
    width: 1200px;
    height: 500px;
    background: var(--canvas-green);
  }
  .label {
    position: absolute;
    left: 305px;
    width: 591px;
    height: 443px;
    box-sizing: border-box;
    border: 22px solid var(--frame-orange);
    background: var(--label-white);
    overflow: hidden;
  }
  .label--on-white { top: 28px; }
  .label--on-green { top: 527px; }

  .label__shimmer {
    position: absolute;
    left: 322px;
    top: 0;
    width: 225px;
    height: 100%;
    background:
      radial-gradient(ellipse 90px 140px at 60px 150px, var(--stripe-glow) 0%, rgba(251,247,166,0) 100%),
      linear-gradient(180deg, #c9a66b 0%, var(--stripe-brown) 100%);
    opacity: 0.85;
  }
  .label__peaks {
    position: absolute;
    left: 0;
    top: 275px;
    width: 324px;
    height: 125px;
    background: linear-gradient(180deg, rgba(17,88,127,0.35) 0%, var(--peak-blue) 100%);
  }
  .label__name {
    position: absolute;
    left: 111px;
    top: 128px;
    margin: 0;
    font-family: "Didact Gothic", "Helvetica Neue", Arial, sans-serif;
    font-weight: 400;
    font-size: 74px;
    line-height: 1;
    letter-spacing: 1px;
    color: var(--name-grey);
  }
</style>
</head>
<body>
<main class="canvas">
  <div class="backdrop-green"></div>

  <section class="label label--on-white">
    <div class="label__shimmer" role="img" aria-label="Vertical sparkling stripe pattern with a pale golden glow"></div>
    <div class="label__peaks" role="img" aria-label="Illustration of snowy blue mountain peaks"></div>
    <h1 class="label__name">Glintova</h1>
  </section>

  <section class="label label--on-green">
    <div class="label__shimmer" role="img" aria-label="Vertical sparkling stripe pattern with a pale golden glow"></div>
    <div class="label__peaks" role="img" aria-label="Illustration of snowy blue mountain peaks"></div>
    <h2 class="label__name">Glintova</h2>
  </section>
</main>
</body>
</html>
```